Maple Hollow Canine Massage Needs a Business Card Design

Maple Hollow Canine Massage is a new therapeutic canine massage company located in Nederland, Colorado. I need a business card design that include my logo and basic contact information.

Target Market(s)

Pet owners, veterinarians

Industry/Entity Type

Business

Contact Information for Business Card

Lydia Ferrow, CCMT
303.518.7269
lydia@maplehollowmassage.example
www.maplehollowmassage.example

Colors
6c459b
886aae
b8a6cd
a64599
b768aa
d3a5cc
fbed22

Requirements
Must have
• Font should be similar to font in logo.

```html
<!DOCTYPE html>
<html lang="en">
<head>
<meta charset="utf-8">
<title>Maple Hollow Canine Massage – Business Card</title>
<link rel="stylesheet" href="https://fonts.googleapis.com/css2?family=Montserrat:wght@400;500;600&display=swap">
<style>
  :root {
    --page-bg: #e6e6e6;
    --card-light: #f3f3f3;
    --logo-field: #f8f8f8;
    --panel-top: #dcdcdc;
    --panel-bottom: #c9c9c9;
    --ink: #1d1d1d;
    --icon-bg: #111111;
    --icon-fg: #ffffff;
    --purple-deep: #6c459b;
    --purple-mid: #886aae;
    --lavender-band: #b083bd;
  }
  * { box-sizing: border-box; margin: 0; padding: 0; }
  html, body {
    width: 1200px; height: 900px; overflow: hidden;
    background: var(--page-bg);
    font-family: "Montserrat", sans-serif;
    color: var(--ink);
  }
  .business-card {
    position: absolute; left: 110px; top: 170px;
    width: 980px; height: 560px;
    background: var(--card-light);
    box-shadow: 0 10px 30px rgba(0,0,0,0.15);
    overflow: hidden;
  }
  .logo-field {
    position: absolute; left: 40px; top: 90px;
    width: 350px; height: 380px;
    background: var(--logo-field);
    display: flex; flex-direction: column; align-items: center; justify-content: center;
    gap: 22px;
  }
  .logo-mark {
    width: 210px; height: 210px; border-radius: 50%;
    background: var(--purple-mid);
  }
  .brand-name {
    font-weight: 600; font-size: 22px; line-height: 1.25;
    color: var(--purple-deep);
    text-align: center; letter-spacing: 0.5px;
    width: 290px;
  }
  .info-panel {
    position: absolute; left: 430px; top: 0;
    width: 550px; height: 560px;
    background: linear-gradient(160deg, var(--panel-top), var(--panel-bottom));
  }
  .info-panel::before {
    content: ""; position: absolute; left: -34px; top: 190px;
    border-top: 30px solid transparent;
    border-bottom: 30px solid transparent;
    border-right: 34px solid var(--panel-top);
  }
  .accent-band {
    position: absolute; left: 0; bottom: 0;
    width: 100%; height: 36px;
    background: var(--lavender-band);
  }
  .person-name {
    position: absolute; left: 70px; top: 140px;
    font-size: 44px; font-weight: 500; letter-spacing: 0.3px;
  }
  .person-title {
    position: absolute; left: 72px; top: 196px;
    font-size: 26px; font-weight: 400; letter-spacing: 1px;
  }
  .contact-list {
    position: absolute; left: 72px; top: 262px;
    list-style: none;
  }
  .contact-item {
    display: flex; align-items: center; gap: 18px;
    font-size: 20px; height: 52px;
  }
  .contact-icon {
    width: 28px; height: 28px; flex: none;
    background: var(--icon-bg); border-radius: 3px;
    display: flex; align-items: center; justify-content: center;
  }
  .contact-icon svg { width: 20px; height: 20px; }
</style>
</head>
<body>
  <main class="business-card">
    <section class="logo-field">
      <div class="logo-mark"></div>
      <div class="brand-name">Maple Hollow Canine Massage</div>
    </section>

    <section class="info-panel">
      <h1 class="person-name">Lydia Ferrow</h1>
      <p class="person-title">CCMT</p>
      <ul class="contact-list">
        <li class="contact-item">
          <span class="contact-icon">
            <svg viewBox="0 0 20 20" fill="none" stroke="#fff" stroke-width="1.6">
              <circle cx="10" cy="10" r="8"/>
              <path d="M7 6.5 L8.5 6 L9.3 8 L8.4 8.8 Q9.2 10.8 11.2 11.6 L12 10.7 L14 11.5 L13.5 13 Q9 13.5 7 6.5 Z" fill="#fff" stroke="none"/>
            </svg>
          </span>
          303.518.7269
        </li>
        <li class="contact-item">
          <span class="contact-icon">
            <svg viewBox="0 0 20 20" fill="none" stroke="#fff" stroke-width="1.4">
              <circle cx="10" cy="10" r="8"/>
              <ellipse cx="10" cy="10" rx="3.5" ry="8"/>
              <path d="M2 10 H18 M3.5 6 H16.5 M3.5 14 H16.5"/>
            </svg>
          </span>
          www.maplehollowmassage.example
        </li>
        <li class="contact-item">
          <span class="contact-icon">
            <svg viewBox="0 0 20 20" fill="none" stroke="#fff" stroke-width="1.6">
              <rect x="3" y="5" width="14" height="10"/>
              <path d="M3 5 L10 11 L17 5"/>
            </svg>
          </span>
          lydia@maplehollowmassage.example
        </li>
      </ul>
      <div class="accent-band"></div>
    </section>
  </main>
</body>
</html>
```